Brintell's Business Card

I need some designs for a new business card including the new logo attached. An old example of our business card is also attached to show all the data that should be included on the new design.
**I added some more examples someone had mocked up**

Contact Information for Business Card

Should include all info on other examples uploaded.

```html
<!DOCTYPE html>
<html lang="en">
<head>
<meta charset="utf-8">
<title>Brintell's Business Card</title>
<link href="https://fonts.googleapis.com/css2?family=Montserrat:wght@400;500;700;800&family=Oswald:wght@400&display=swap" rel="stylesheet">
<style>
  :root {
    --bg: #ababab;
    --card-white: #ffffff;
    --brand-blue: #0a6bb8;
    --brand-red: #e3202a;
    --text-grey: #5f5f5f;
    --dot-grey: #bdbdbd;
    --badge-grey: #a9a9a9;
    --grad-red: #d9202f;
    --grad-purple: #6a477a;
    --grad-blue: #1f66ad;
  }
  * { margin: 0; padding: 0; box-sizing: border-box; }
  html, body { width: 1200px; height: 1000px; overflow: hidden; }
  body { background: var(--bg); position: relative; font-family: "Montserrat", sans-serif; }

  .card { position: absolute; width: 352px; height: 612px; border-radius: 24px; overflow: hidden; }
  .card--front { left: 205px; top: 202px; background: var(--card-white); text-align: center; }
  .card--back { left: 640px; top: 194px; background: linear-gradient(135deg, var(--grad-red) 0%, var(--grad-purple) 50%, var(--grad-blue) 100%); }

  .tagline-top {
    position: absolute; top: 28px; left: 0; right: 0;
    font-family: "Oswald", sans-serif; font-size: 10px; letter-spacing: 2.2px;
    color: var(--brand-red); text-transform: uppercase;
  }

  .brand-mark { position: absolute; top: 88px; left: 50%; width: 64px; height: 64px; margin-left: -32px; border-radius: 50%; background: var(--brand-blue); }
  .brand-name {
    position: absolute; top: 180px; left: 0; right: 0;
    font-weight: 800; font-size: 42px; line-height: 1; color: var(--brand-blue); letter-spacing: 0.5px;
  }
  .brand-service {
    position: absolute; top: 226px; left: 0; right: 0;
    font-weight: 700; font-size: 10.5px; color: var(--brand-red); text-transform: uppercase;
  }

  .person-name { position: absolute; top: 283px; left: 0; right: 0; font-weight: 500; font-size: 25px; color: var(--brand-blue); }

  .contact-icons { position: absolute; top: 343px; left: 0; right: 0; display: flex; justify-content: center; align-items: center; gap: 6px; }
  .dots { width: 52px; height: 3px; background-image: radial-gradient(circle, var(--dot-grey) 1.4px, transparent 1.6px); background-size: 5px 3px; }
  .icon { width: 24px; height: 24px; border-radius: 5px; background: var(--brand-red); display: flex; align-items: center; justify-content: center; }

  .contact-list { position: absolute; top: 384px; left: 0; right: 0; color: var(--text-grey); font-size: 15.5px; letter-spacing: 0.4px; line-height: 19px; }
  .contact-list p { margin-bottom: 8px; }
  .contact-list .address { margin-top: 0; }

  .badge { position: absolute; top: 498px; left: 50%; margin-left: -44px; }

  .back-mark { position: absolute; top: 220px; left: 50%; width: 170px; height: 170px; margin-left: -85px; border-radius: 50%; background: rgba(255,255,255,0.14); }
</style>
</head>
<body>
  <section class="card card--front">
    <p class="tagline-top">• Family owned &amp; operated •</p>
    <div class="brand-mark" aria-hidden="true"></div>
    <h1 class="brand-name">BRINTELL'S</h1>
    <p class="brand-service">Air Conditioning &amp; Heating Service</p>
    <h2 class="person-name">Dylan Marsh</h2>

    <div class="contact-icons">
      <span class="dots"></span>
      <span class="icon">
        <svg width="14" height="14" viewBox="0 0 24 24"><path fill="#fff" d="M6.6 10.8a15.1 15.1 0 0 0 6.6 6.6l2.2-2.2c.3-.3.7-.4 1-.2 1.1.4 2.3.6 3.6.6.6 0 1 .4 1 1V20c0 .6-.4 1-1 1A17 17 0 0 1 3 4c0-.6.4-1 1-1h3.5c.6 0 1 .4 1 1 0 1.3.2 2.5.6 3.6.1.3 0 .7-.2 1z"/></svg>
      </span>
      <span class="icon">
        <svg width="16" height="12" viewBox="0 0 16 12"><rect x="1" y="1" width="14" height="10" rx="1" fill="none" stroke="#fff" stroke-width="1.5"/><path d="M1.5 1.5 8 7l6.5-5.5" fill="none" stroke="#fff" stroke-width="1.5"/></svg>
      </span>
      <span class="icon">
        <svg width="12" height="16" viewBox="0 0 12 16"><path fill="#fff" d="M6 0a6 6 0 0 0-6 6c0 4.5 6 10 6 10s6-5.5 6-10a6 6 0 0 0-6-6zm0 8.3A2.3 2.3 0 1 1 6 3.7a2.3 2.3 0 0 1 0 4.6z"/></svg>
      </span>
      <span class="dots"></span>
    </div>

    <div class="contact-list">
      <p>555.014.2270</p>
      <p>hvacbrintell@inbox.com</p>
      <p class="address">418 Alder Lane<br>Ridgeview, IA 50000, EUA</p>
    </div>

    <svg class="badge" width="88" height="88" viewBox="0 0 88 88" role="img" aria-label="Licensed and insured seal">
      <circle cx="44" cy="44" r="42" fill="none" stroke="var(--badge-grey)" stroke-width="1.2"/>
      <circle cx="44" cy="44" r="28" fill="none" stroke="var(--badge-grey)" stroke-width="1.2"/>
      <path d="M32 44l8 9 16-18" fill="none" stroke="var(--badge-grey)" stroke-width="5" stroke-linecap="round" stroke-linejoin="round"/>
    </svg>
  </section>

  <section class="card card--back">
    <div class="back-mark" role="img" aria-label="Brand mark area"></div>
  </section>
</body>
</html>
```